Banner Design 4040mm W x 2190mm H

Design a glamorous and exciting 4040mm W x 2190mm H backdrop for the QRLMT Velvet Orchid Gala at the luxurious Tallow Hall, Fenwick, Mirrabelle, Sydney. This exciting backdrop should be spectacular so that people will be excited to take photos in front of it.
Design Colours preferred is black and pink.
Please include our website on the banner www.qrlmt.org.au
Should include the words "QRLMT Velvet Orchid Gala" as the main attraction on the banner.
Please include "Thank you to our sponsors" and include the logo of the sponsors.
Sponsors:
Brockden Pathology
EastGlen Radiology
KTV Diagnostic Imaging
Harbin Legal Group
Truffords
Banner Template:
4040mm W x 2190mm H Single Sided (.AI)
https://files.example-share.net/d/8ZkQm3TnWp47LcVbXr2YhJd5Fs61Ae/view
QRLMT Logo:
Can be obtained from our website www.qrlmt.org.au

```html
<!DOCTYPE html>
<html lang="en">
<head>
<meta charset="utf-8">
<title>QRLMT Velvet Orchid Gala – Backdrop</title>
<link rel="stylesheet" href="https://fonts.googleapis.com/css2?family=Great+Vibes&family=Montserrat:wght@500;600;700&family=Poppins:wght@600&display=swap">
<style>
  :root {
    --page-bg: #a6a6a6;
    --blush: #f7cfdd;
    --rose: #e58fae;
    --magenta: #c2326f;
    --plum: #8e1450;
    --hot-pink: #f23bd6;
    --wine: #6e1446;
    --gold: #ffe500;
    --orange: #ff8a1e;
    --white: #ffffff;
    --ink: #2b2b4a;
    --sponsor: #4a3a8c;
  }
  * { margin: 0; padding: 0; box-sizing: border-box; }
  html, body { width: 800px; height: 1200px; overflow: hidden; }
  body { background: var(--page-bg); position: relative; }

  .backdrop {
    position: absolute; left: 20px; top: 394px;
    width: 760px; height: 412px; overflow: hidden;
    background:
      radial-gradient(ellipse 260px 200px at 600px 150px, rgba(110,15,70,.55), transparent 70%),
      linear-gradient(90deg, var(--blush) 0%, #f2b9cd 30%, var(--rose) 44%, var(--magenta) 64%, var(--plum) 86%, #a01a5c 100%);
    box-shadow: 6px 8px 14px rgba(0,0,0,.35);
  }

  .floral-frame {
    position: absolute; left: 21px; top: 15px; width: 270px; height: 385px;
    background: radial-gradient(ellipse at center, #f7dbe6 45%, #e9a9c0 72%, #b9c79f 100%);
  }

  .sponsor-panel {
    position: absolute; left: 65px; top: 62px; width: 181px; height: 290px;
    background: var(--white);
    box-shadow: 0 0 10px rgba(255,255,255,.9);
    text-align: center;
  }
  .thanks-title {
    font-family: "Great Vibes", cursive;
    color: var(--wine); font-size: 56px; line-height: 1;
    margin-top: 20px;
  }
  .thanks-you {
    font-family: "Great Vibes", cursive;
    color: var(--hot-pink); font-size: 46px; line-height: .9;
  }
  .thanks-caption {
    font-family: "Poppins", sans-serif; font-weight: 600;
    font-size: 10px; letter-spacing: 1.6px; color: var(--ink);
    margin-top: 8px;
  }
  .sponsor-list {
    position: absolute; left: 12px; right: 8px; top: 172px;
    display: grid; grid-template-columns: 1fr 1fr; gap: 12px 6px;
    text-align: left;
  }
  .sponsor {
    display: flex; align-items: center; gap: 4px;
    font-family: "Montserrat", sans-serif; font-weight: 600;
    font-size: 8.5px; line-height: 1.15; color: var(--sponsor);
  }
  .sponsor .mark { flex: none; width: 10px; height: 10px; background: var(--sponsor); }
  .sponsor .mark.round { border-radius: 50%; }

  .client-mark {
    position: absolute; left: 332px; top: 98px;
    display: flex; align-items: center; gap: 8px;
    font-family: "Montserrat", sans-serif; font-weight: 600;
    font-size: 22px; line-height: 1; color: var(--white);
  }
  .client-mark .mark { flex: none; width: 20px; height: 20px; border-radius: 50%; background: var(--white); }

  .gala-title { position: absolute; inset: 0; font-weight: normal; }
  .gala-org {
    position: absolute; right: 41px; top: 33px;
    font-family: "Montserrat", sans-serif; font-weight: 600;
    font-size: 64px; line-height: 1;
    background: linear-gradient(90deg, var(--gold) 0%, var(--gold) 35%, var(--orange) 100%);
    -webkit-background-clip: text; background-clip: text; color: transparent;
  }
  .gala-velvet {
    position: absolute; right: 40px; top: 100px;
    font-family: "Great Vibes", cursive; font-size: 92px; line-height: 1.1;
    padding-right: 6px;
    background: linear-gradient(90deg, var(--hot-pink), #d21fd0);
    -webkit-background-clip: text; background-clip: text; color: transparent;
  }
  .gala-orchid {
    position: absolute; right: 41px; top: 209px;
    font-family: "Montserrat", sans-serif; font-weight: 600;
    font-size: 84px; line-height: 1; color: var(--white);
  }
  .gala-word {
    position: absolute; right: 42px; top: 262px;
    font-family: "Great Vibes", cursive; font-size: 70px; line-height: 1;
    color: var(--gold);
  }
  .gala-site {
    position: absolute; right: 43px; top: 348px;
    font-family: "Montserrat", sans-serif; font-weight: 500;
    font-size: 24px; line-height: 1; letter-spacing: 5px; color: var(--white);
  }
  .gala-site b { font-weight: 700; color: var(--gold); }
</style>
</head>
<body>
  <section class="backdrop">
    <div class="floral-frame" role="img" aria-label="Ornate white picture frame wreathed in pink and white flowers with green leaves"></div>
    <div class="sponsor-panel">
      <div class="thanks-title">Thank</div>
      <div class="thanks-you">you</div>
      <div class="thanks-caption">TO OUR SPONSORS</div>
      <div class="sponsor-list">
        <div class="sponsor"><span class="mark"></span>Brockden Pathology</div>
        <div class="sponsor"><span class="mark"></span>Harbin Legal Group</div>
        <div class="sponsor"><span class="mark round"></span>EastGlen Radiology</div>
        <div class="sponsor"><span class="mark"></span>Truffords</div>
        <div class="sponsor"><span class="mark round"></span>KTV Diagnostic Imaging</div>
      </div>
    </div>

    <div class="client-mark"><span class="mark"></span>QRLMT</div>

    <h1 class="gala-title">
      <span class="gala-org">QRLMT</span>
      <span class="gala-velvet">Velvet</span>
      <span class="gala-orchid">ORCHID</span>
      <span class="gala-word">Gala</span>
    </h1>
    <p class="gala-site">www.<b>qrlmt</b>.org.au</p>
  </section>
</body>
</html>
```